Im want a website LIKE KMT's and FleetStride.com's with product payment options like Wendaro's

I need a website LIKE KMT with a header made EXACTLY LIKE THAT OF FLEETSTRIDES .

The front page photo should be like that of FLEETSTRIDE's webpage as well.

The name of the website will be called "C.M. (Calmira Mesa)".

We will be targeting ALL MARKETS in a small town in central Panama and charging businesses "listing fees" like a phone book does but also providing informational blogs, news, and other interesting activities.

THIS IS A MULTI PAGE WEBSITE

THIS IS WHERE KMT's website meets Norvex/FleetStride.

Once the layout is built I will tweak and modify, add information, and upload items for sale.

Here is a list of specific categories that should be listed out above the front page header image/search bar

-- Home -- News -- Travel -- Activities -- Shop & Dine -- Store -- More... --

These categories should be spread across the bottom of the page in three sections:

WHATS SO GREAT ABOUT (Calmira Mesa),
HAND PICKED TOURS
ACTIVITIES etc.

Also lets use www.Wendaro.example 's
"HOT DESTINATIONS"
"BEAT THE BEST PRICES IN CALMIRA"
"OCTOBERS INSIDER PICKS"
"TOP DESTINATIONS"
and spread them in four sections side-by-side near the bottom of the page.

Overall I would like to see the finished product to be something LIKE KMT's and FleetStrides.

WE NEED ONLINE PAYMENT OPTIONS LIKE NORVEX'S WEBSITE HAS

This will be a desktop website but should be very mobile friendly as well.

-rodwell

P.S. Good luck!
Updates

If it isn't already too late to change the website name, the name of the website should be "Calmira Mesa". Added Friday, October 9, 2015

What do you guys think the budget should be to win this? Added Saturday, October 10, 2015

www.lunaverde.example is the most amazing simple site. Whoever can make me a replica with my specifications will win immediately!!!! Added Sunday, October 18, 2015

OMG www.lunaverde.example is the bomb!So simple and elegant. Whoever can make me an EXACT REPLICA OF WWW.LUNAVERDE.EXAMPLE as my site with the specifications mentioned in my brief will take home the $825.00 immediately! Good luck amigos! Added Sunday, October 18, 2015

Does anybody know how to add recurring monthly billing options on this website? Added Sunday, October 18, 2015

Target Market(s)

ALL MARKETS

Industry/Entity Type

Product

Coding

Coded - Design and coding required

Number of Pages Required

5+ page

Requirements
Must have
• Coinlark payment options.
• I must be able to add and remove photos/text and video from the HTML files in the page.
• Be creative my friends, and may the odds be forever in your favor!
Nice to have
• I added some photos of a good layout for our page below.

```html
<!DOCTYPE html>
<html lang="en">
<head>
<meta charset="utf-8">
<title>Calmira Mesa</title>
<link rel="stylesheet" href="https://fonts.googleapis.com/css2?family=Open+Sans:wght@400;600;700&display=swap">
<style>
:root{
  --ink:#333;
  --muted:#777;
  --line:#d8d8d8;
  --brand:#2a9fd6;
  --brand-dark:#1b78b5;
  --green:#5aa832;
  --band:#f6f6f6;
  --cream:#fdf5cf;
  --cap:rgba(20,30,40,.72);
  --white:#fff;
}
*{box-sizing:border-box;margin:0;padding:0}
html,body{width:1200px;height:2872px;overflow:hidden}
body{font-family:"Open Sans",Arial,sans-serif;color:var(--ink);background:var(--white);font-size:12px}
.wrap{width:870px;margin:0 auto;position:relative}

/* header */
.site-header{height:84px;display:flex;align-items:center}
.site-header .wrap{display:flex;align-items:center;justify-content:space-between}
.brand{display:flex;align-items:center;gap:8px;font-size:26px;font-weight:700;color:var(--brand)}
.brand-dot{width:14px;height:14px;border-radius:50%;background:var(--green)}
.main-nav{display:flex;gap:16px;font-size:10px;font-weight:600;color:var(--ink)}

/* hero */
.hero{height:300px;position:relative;background:linear-gradient(180deg,#6f8fa8 0%,#e8c07a 48%,#f4d693 56%,#41505a 80%,#2a2f33 100%)}
.hero-title{position:absolute;left:0;right:0;top:160px;text-align:center;color:var(--white);font-size:30px;font-weight:700;letter-spacing:1px}
.hero-arrow{position:absolute;top:138px;width:26px;height:26px;border-radius:50%;background:rgba(0,0,0,.45)}
.hero-arrow.prev{left:120px}.hero-arrow.next{right:120px}
.hero-arrow svg{display:block}
.hero-dots{position:absolute;bottom:14px;left:0;right:0;display:flex;justify-content:center;gap:6px}
.hero-dots span{width:8px;height:8px;border-radius:50%;background:rgba(255,255,255,.6)}
.hero-dots span.on{background:var(--white)}

/* section titles */
.section-title{display:flex;align-items:center;gap:16px;height:40px;font-size:18px;font-weight:700;color:#444}
.section-title::before,.section-title::after{content:"";flex:1;height:1px;background:var(--line)}

/* tile grid */
.tile-grid{display:grid;grid-template-columns:repeat(3,282px);grid-auto-rows:192px;gap:12px}
.tile{position:relative;overflow:hidden}
.tile-caption{position:absolute;left:50%;bottom:16px;transform:translateX(-50%);width:200px;background:var(--cap);color:var(--white);text-align:center;padding:5px 8px;font-size:10px;line-height:1.35}
.tile-caption b{display:block;font-size:11px}
.g-beach{background:linear-gradient(160deg,#5fb6dd,#2f8fb8 50%,#e6dcc0 80%)}
.g-palm{background:linear-gradient(180deg,#3b84c4,#7fc0e0 55%,#2e5a3a 100%)}
.g-drink{background:linear-gradient(160deg,#7ec3e5,#f29a3b 55%,#d8652a)}
.g-isle{background:linear-gradient(180deg,#7fb9dc,#e9f1f6 45%,#2b8db1 70%,#1f5f7d)}
.g-ship{background:linear-gradient(180deg,#5e7d99,#c8cfd5 55%,#6a7580)}
.g-hotel{background:linear-gradient(170deg,#9ac3e0,#d6d6d0 50%,#7e8d7a)}
.g-pool{background:linear-gradient(180deg,#2a5d86,#2fa3c7 55%,#6cc0d6)}
.g-room{background:linear-gradient(160deg,#6b3f26,#c48a58 55%,#efe0c8)}
.g-fruit{background:linear-gradient(150deg,#e2a12e,#b5442b 55%,#4d7a2c)}
.g-shop{background:linear-gradient(160deg,#d6dde3,#9fb3c2 55%,#5b6d7a)}
.g-food{background:linear-gradient(150deg,#c9902f,#e8c277 50%,#8a5b2a)}
.g-plate{background:linear-gradient(160deg,#4f3b2c,#d2b17a 55%,#f0e6d0)}

/* search box */
.search-box{background:linear-gradient(180deg,var(--brand),var(--brand-dark));color:var(--white);padding:14px 16px}
.search-box h3{font-size:13px;font-weight:700;text-align:center;margin-bottom:10px}
.search-box label{display:block;font-size:9px;margin-bottom:3px}
.search-box .field{height:20px;background:var(--white);margin-bottom:8px}
.search-box .row{display:flex;gap:8px}.search-box .row>div{flex:1}
.search-box .btn{display:inline-block;margin-top:4px;padding:4px 14px;background:var(--green);font-size:10px;font-weight:700}

/* insider band */
.insider{background:var(--band);height:268px;margin-top:40px;padding-top:26px}
.insider .wrap{display:grid;grid-template-columns:282px 282px 282px;gap:12px}
.insider h4{font-size:11px;font-weight:700;color:var(--brand-dark);display:flex;align-items:center;gap:6px;margin-bottom:10px}
.insider h4 i{width:12px;height:12px;border-radius:50%;background:var(--brand);display:inline-block}
.link-list{list-style:none;font-size:9.5px;line-height:2.05;color:#555}
.link-list li{display:flex;align-items:center;gap:6px;border-bottom:1px dotted var(--line)}
.link-list li::before{content:"";width:5px;height:5px;border-radius:50%;background:var(--brand)}
.two-col{display:grid;grid-template-columns:1fr 1fr;gap:14px}
.insider p{font-size:9.5px;line-height:1.5;color:var(--muted);margin-bottom:10px}
.deal{display:grid;grid-template-columns:110px 1fr;gap:12px}
.deal-img{height:90px;background:linear-gradient(180deg,#7fc6e6,#2f9cbf 60%,#e8dcb8)}

.block{margin-top:20px}
.block .tile-grid{margin-top:16px}

/* newsletter */
.newsletter{background:var(--cream);height:220px;margin-top:48px;padding-top:26px}
.newsletter .wrap{display:grid;grid-template-columns:380px 1fr;gap:80px}
.newsletter h4{font-size:13px;font-weight:700;margin-bottom:6px}
.newsletter p{font-size:9.5px;color:var(--muted);margin-bottom:10px}
.newsletter .field{height:22px;background:var(--white);border:1px solid #e2dcb8;margin-bottom:8px;font-size:9px;color:#aaa;padding:4px 8px}
.newsletter .btn{display:inline-block;padding:5px 14px;background:#333;color:var(--white);font-size:10px;font-weight:700}
.ads{display:grid;grid-template-columns:1fr 1fr;grid-auto-rows:80px;gap:8px}
.ad-a{background:linear-gradient(135deg,#1c1c2e,#7a2c6a)}
.ad-b{background:linear-gradient(135deg,#f3c64a,#e24a2b)}
.ad-c{background:linear-gradient(135deg,#2b2b2b,#c8357a)}
.ad-d{background:linear-gradient(135deg,#d8e9f2,#6a8fb0)}

.shop{margin-top:32px}
.shop .tile-grid{margin-top:16px}
</style>
</head>
<body>

<header class="site-header">
  <div class="wrap">
    <div class="brand"><span class="brand-dot"></span>Calmira Mesa</div>
    <nav class="main-nav">
      <span>Home</span><span>News</span><span>Travel</span><span>Activities</span><span>Shop &amp; Dine</span><span>Store</span><span>Weather</span><span>Contact</span><span>Login</span><span>Sign Up</span>
    </nav>
  </div>
</header>

<section class="hero" role="img" aria-label="Sunset over a rocky beach with calm sea">
  <div class="hero-arrow prev"><svg width="26" height="26"><path d="M15 8l-5 5 5 5" stroke="#fff" stroke-width="2" fill="none"/></svg></div>
  <div class="hero-title">LOREM IPSUM DOLOR SIT AMET</div>
  <div class="hero-arrow next"><svg width="26" height="26"><path d="M11 8l5 5-5 5" stroke="#fff" stroke-width="2" fill="none"/></svg></div>
  <div class="hero-dots"><span class="on"></span><span></span><span></span><span></span><span></span></div>
</section>

<section class="wrap block" style="margin-top:32px">
  <h2 class="section-title">Discover Calmira Mesa</h2>
  <div class="tile-grid">
    <div class="tile g-beach" role="img" aria-label="Turquoise beach with palm trees"><div class="tile-caption"><b>Lorem ipsum dolor sit amet</b>Colored White Sand Beach - Tabs</div></div>
    <div class="tile g-palm" role="img" aria-label="Palm trees on a tropical shore"><div class="tile-caption"><b>Lorem ipsum dolor sit amet</b>Colored White Sand Beach - Tabs</div></div>
    <div class="search-box">
      <h3>Search Tours In Calmira</h3>
      <label>Destination</label><div class="field"></div>
      <div class="row"><div><label>From</label><div class="field"></div></div><div><label>To</label><div class="field"></div></div></div>
      <label>Category</label><div class="field"></div>
      <span class="btn">Search</span>
    </div>
    <div class="tile g-drink" role="img" aria-label="Tropical cocktail on a beach"><div class="tile-caption"><b>Lorem ipsum dolor sit amet</b>Colored White Sand Beach - Tabs</div></div>
    <div class="tile g-isle" role="img" aria-label="Island seen across clear water"><div class="tile-caption"><b>Lorem ipsum dolor sit amet</b>Colored White Sand Beach - Tabs</div></div>
    <div class="tile g-ship" role="img" aria-label="Cruise ship at sea"><div class="tile-caption"><b>Lorem ipsum dolor sit amet</b>Colored White Sand Beach - Tabs</div></div>
  </div>
</section>

<section class="insider">
  <div class="wrap">
    <div>
      <h4><i></i>Hot Destination</h4>
      <div class="two-col">
        <ul class="link-list"><li>Valle Alto</li><li>Rio Claro</li><li>Las Nubes</li><li>Playa Serena</li><li>Cerro Verde</li><li>Puerto Lindo</li><li>Los Pinos</li><li>Santa Rita</li></ul>
        <ul class="link-list"><li>El Mirador</li><li>Isla Bonita</li><li>Agua Dulce</li><li>Las Flores</li><li>Monte Azul</li><li>Bahía Sol</li><li>Río Bravo</li><li>Palmar</li></ul>
      </div>
    </div>
    <div>
      <h4><i></i>Beat The Best Prices In Calmira</h4>
      <p>Why pay more? Compare local tours and stays, then book the best deal in one simple place.</p>
      <div class="deal">
        <div class="deal-img" role="img" aria-label="Sunny beach with clear water"></div>
        <ul class="link-list"><li>Beach Hotels</li><li>Tour Packages</li><li>Coffee Farms</li><li>Local Guides</li><li>River Rafting</li></ul>
      </div>
    </div>
    <div>
      <h4><i></i>Travelers Insider Picks</h4>
      <ul class="link-list"><li>Hike the cloud forest trail at dawn</li><li>Taste fresh coffee at a mountain farm</li><li>Ride the rapids on the upper river</li><li>Relax in the hot springs after a hike</li><li>Watch birds in the quiet highlands</li><li>Walk the weekend craft market</li><li>Zip line above the forest canopy</li><li>Dine on local food in the town square</li></ul>
    </div>
  </div>
</section>

<section class="wrap block">
  <h2 class="section-title">Accomodation</h2>
  <div class="tile-grid">
    <div class="tile g-hotel" role="img" aria-label="Hotel towers by the sea"><div class="tile-caption"><b>Lorem ipsum dolor sit amet</b>Colored White Sand Beach - Tabs</div></div>
    <div class="tile g-pool" role="img" aria-label="Resort pool at night"><div class="tile-caption"><b>Lorem ipsum dolor sit amet</b>Colored White Sand Beach - Tabs</div></div>
    <div class="tile g-room" role="img" aria-label="Warm hotel room interior"><div class="tile-caption"><b>Lorem ipsum dolor sit amet</b>Colored White Sand Beach - Tabs</div></div>
    <div class="tile g-drink" role="img" aria-label="Tropical cocktail on a beach"><div class="tile-caption"><b>Lorem ipsum dolor sit amet</b>Colored White Sand Beach - Tabs</div></div>
    <div class="tile g-isle" role="img" aria-label="Island seen across clear water"><div class="tile-caption"><b>Lorem ipsum dolor sit amet</b>Colored White Sand Beach - Tabs</div></div>
    <div class="tile g-ship" role="img" aria-label="Cruise ship at sea"><div class="tile-caption"><b>Lorem ipsum dolor sit amet</b>Colored White Sand Beach - Tabs</div></div>
  </div>
</section>

<section class="wrap block" style="margin-top:36px">
  <h2 class="section-title">Activities</h2>
  <div class="tile-grid">
    <div class="tile g-hotel" role="img" aria-label="Hotel towers by the sea"><div class="tile-caption"><b>Lorem ipsum dolor sit amet</b>Colored White Sand Beach - Tabs</div></div>
    <div class="tile g-pool" role="img" aria-label="Resort pool at night"><div class="tile-caption"><b>Lorem ipsum dolor sit amet</b>Colored White Sand Beach - Tabs</div></div>
    <div class="tile g-room" role="img" aria-label="Warm hotel room interior"><div class="tile-caption"><b>Lorem ipsum dolor sit amet</b>Colored White Sand Beach - Tabs</div></div>
    <div class="tile g-drink" role="img" aria-label="Tropical cocktail on a beach"><div class="tile-caption"><b>Lorem ipsum dolor sit amet</b>Colored White Sand Beach - Tabs</div></div>
    <div class="tile g-isle" role="img" aria-label="Island seen across clear water"><div class="tile-caption"><b>Lorem ipsum dolor sit amet</b>Colored White Sand Beach - Tabs</div></div>
    <div class="tile g-ship" role="img" aria-label="Cruise ship at sea"><div class="tile-caption"><b>Lorem ipsum dolor sit amet</b>Colored White Sand Beach - Tabs</div></div>
  </div>
</section>

<section class="newsletter">
  <div class="wrap">
    <div>
      <h4>Email Newsletter</h4>
      <p>Join our newsletter to get the latest deals and local news.</p>
      <div class="field">Your name</div>
      <div class="field">Your email address</div>
      <span class="btn">Subscribe</span>
    </div>
    <div class="ads">
      <div class="ad-a" role="img" aria-label="Promotional banner for a night event"></div>
      <div class="ad-b" role="img" aria-label="Promotional banner for a discount sale"></div>
      <div class="ad-c" role="img" aria-label="Promotional banner for a beauty shop"></div>
      <div class="ad-d" role="img" aria-label="Promotional banner for a travel offer"></div>
    </div>
  </div>
</section>

<section class="wrap shop">
  <h2 class="section-title">Shop &amp; Dine</h2>
  <div class="tile-grid">
    <div class="tile g-fruit" role="img" aria-label="Fresh tropical fruit at a market"><div class="tile-caption"><b>Lorem ipsum dolor sit amet</b>Colored White Sand Beach - Tabs</div></div>
    <div class="tile g-shop" role="img" aria-label="Clothing boutique interior"><div class="tile-caption"><b>Lorem ipsum dolor sit amet</b>Colored White Sand Beach - Tabs</div></div>
    <div class="tile g-food" role="img" aria-label="Plated local dish"><div class="tile-caption"><b>Lorem ipsum dolor sit amet</b>Colored White Sand Beach - Tabs</div></div>
    <div class="tile g-drink" role="img" aria-label="Tropical cocktail on a beach"><div class="tile-caption"><b>Lorem ipsum dolor sit amet</b>Colored White Sand Beach - Tabs</div></div>
    <div class="tile g-shop" role="img" aria-label="Shop counter with goods"><div class="tile-caption"><b>Lorem ipsum dolor sit amet</b>Colored White Sand Beach - Tabs</div></div>
    <div class="tile g-plate" role="img" aria-label="Pastries served on a plate"><div class="tile-caption"><b>Lorem ipsum dolor sit amet</b>Colored White Sand Beach - Tabs</div></div>
  </div>
</section>

</body>
</html>
```